Meadowlark Counseling Business Card Design Project

I am starting a new business that provides counseling and coaching services to individuals and couples. These individuals are people looking to "transform" or grow in the personal lives. The design should convey trust, intimacy, hope, growth. It should be professional, elegant.
Contact information
Name: Dana R. Whitcombe
Title: Counselor and Life Coach
Slogan: Bringing Hope. Renewing Lives.
address: 47310 County Road 9, Suite 410
Plymouth, MN 55490
Phone: 763-555-0184
Email: dana@meadowlark-cx.example
website: www.meadowlark-cx.example
Back side of card should have bullets:
Individual counseling
Relationship counseling
Life Coaching for Teens and Adults
Group Workshops

```html
<!DOCTYPE html>
<html lang="en">
<head>
<meta charset="utf-8">
<title>Meadowlark Counseling – Business Card</title>
<link href="https://fonts.googleapis.com/css2?family=Crimson+Text:wght@400;600&display=swap" rel="stylesheet">
<style>
  :root {
    --stage: #c8c8c8;
    --paper: #ffffff;
    --blue-light: #239fda;
    --blue-mid: #1b7fb9;
    --blue-dark: #1d3b63;
    --brand-blue: #1f5a8c;
    --ink: #555555;
    --icon: #1f4f86;
  }
  * { margin: 0; padding: 0; box-sizing: border-box; }
  html, body { width: 1200px; height: 900px; overflow: hidden; }
  body {
    background: var(--stage);
    font-family: "Crimson Text", Georgia, serif;
    position: relative;
  }
  .card {
    position: absolute;
    left: 246px;
    width: 704px;
    height: 392px;
    overflow: hidden;
  }
  /* Front */
  .card-front {
    top: 44px;
    background: radial-gradient(ellipse at 25% 50%, var(--blue-light) 0%, var(--blue-mid) 45%, var(--blue-dark) 100%);
  }
  .stripe-band {
    position: absolute;
    left: 0;
    width: 100%;
    height: 80px;
    background: linear-gradient(90deg, #1f8cc6 0%, #1a5f95 55%, #1a3558 100%);
  }
  .stripe-band.top { top: 0; }
  .stripe-band.bottom { bottom: 0; height: 79px; }
  .front-mark {
    position: absolute;
    left: 56px; top: 118px;
    width: 72px; height: 72px;
    border-radius: 50%;
    background: #c9d3dc;
  }
  .front-name {
    position: absolute;
    left: 178px; top: 128px;
    width: 472px;
    color: #ffffff;
    font-weight: 400;
    text-align: center;
  }
  .front-name .line-main {
    display: block; font-size: 46px; letter-spacing: 1px; line-height: 1.05; text-transform: uppercase;
  }
  .front-name .rule {
    display: block; width: 300px; height: 1px; margin: 0 auto;
    background: rgba(255,255,255,0.55);
  }
  .front-name .line-sub {
    display: block; font-size: 21px; letter-spacing: 8.4px; margin-right: -8.4px;
    text-transform: uppercase; line-height: 1.4;
  }
  .services {
    position: absolute;
    left: 0; top: 230px;
    width: 822px;
    text-align: center;
    color: #ffffff;
    font-size: 20px;
    line-height: 34px;
  }
  .services .row { display: block; }
  .services .sep { display: inline-block; width: 1px; height: 24px; background: #ffffff; vertical-align: middle; margin: 0 6px; }

  /* Back */
  .card-back {
    top: 455px;
    background: var(--paper);
  }
  .back-mark {
    position: absolute;
    left: 162px; top: 26px;
    width: 56px; height: 56px;
    border-radius: 50%;
    background: var(--brand-blue);
  }
  .back-name {
    position: absolute;
    left: 244px; top: 38px;
    width: 322px;
    color: var(--brand-blue);
    font-weight: 400;
    text-align: center;
  }
  .back-name .line-main { display: block; font-size: 32px; letter-spacing: 0.5px; line-height: 1; text-transform: uppercase; }
  .back-name .rule { display: block; width: 200px; height: 1px; margin: 2px auto 0; background: rgba(31,90,140,0.5); }
  .back-name .line-sub {
    display: block; font-size: 14px; letter-spacing: 5.8px; margin-right: -5.8px;
    text-transform: uppercase; margin-top: 4px; color: #444;
  }
  .slogan-band {
    position: absolute;
    left: 0; top: 120px;
    width: 100%; height: 56px;
    background: linear-gradient(90deg, #2186c0 0%, #22a0dc 50%, #1d78b4 100%);
  }
  .slogan {
    position: absolute;
    left: 0; top: 120px;
    width: 100%; height: 56px;
    line-height: 56px;
    text-align: center;
    color: #ffffff;
    font-size: 27px;
    font-weight: 600;
    letter-spacing: 0.3px;
  }
  .person {
    position: absolute;
    left: 244px; top: 200px;
    color: var(--ink);
  }
  .person-name { color: var(--brand-blue); font-size: 23px; line-height: 1.2; }
  .person-role { font-size: 18px; line-height: 1.2; }
  .contact {
    position: absolute;
    left: 244px; top: 293px;
    list-style: none;
    color: var(--ink);
    font-size: 15.5px;
  }
  .contact li { display: flex; align-items: center; height: 20px; }
  .contact svg { width: 16px; height: 16px; margin-right: 8px; flex: none; }
</style>
</head>
<body>

<section class="card card-front" aria-label="Card front">
  <div class="stripe-band top" role="img" aria-label="Diagonal stripe pattern band"></div>
  <div class="stripe-band bottom" role="img" aria-label="Diagonal stripe pattern band"></div>
  <span class="front-mark" aria-hidden="true"></span>
  <h1 class="front-name">
    <span class="line-main">Meadowlark</span>
    <span class="rule" aria-hidden="true"></span>
    <span class="line-sub">Counseling and Coaching</span>
  </h1>
  <p class="services">
    <span class="row">Individual Counseling<span class="sep"></span>Relationship Counseling</span>
    <span class="row">Life Coaching for Teens and Adults <span class="sep"></span>Group Workshops</span>
  </p>
</section>

<section class="card card-back" aria-label="Card back">
  <span class="back-mark" aria-hidden="true"></span>
  <h2 class="back-name">
    <span class="line-main">Meadowlark</span>
    <span class="rule" aria-hidden="true"></span>
    <span class="line-sub">Counseling and Coaching</span>
  </h2>
  <div class="slogan-band" role="img" aria-label="Diagonal stripe pattern band"></div>
  <p class="slogan">Bringing Hope. Renewing Lives.</p>

  <div class="person">
    <p class="person-name">Dana R. Whitcombe</p>
    <p class="person-role">Counselor • Life Coach</p>
    <p class="person-role">Meadowlark Counseling and Coaching, LLC</p>
  </div>

  <ul class="contact">
    <li>
      <svg viewBox="0 0 16 16"><circle cx="8" cy="8" r="8" fill="var(--icon)"/><path d="M8 3.5 3.5 7.6h1.3v4.4h2.3V9.4h1.8V12h2.3V7.6h1.3z" fill="#fff"/></svg>
      47310 County Road 9, Suite 410, Plymouth, MN 55490
    </li>
    <li>
      <svg viewBox="0 0 16 16"><circle cx="8" cy="8" r="8" fill="var(--icon)"/><path d="M5.2 3.8c.4-.3.9-.2 1.1.2l.8 1.4c.2.4.1.8-.2 1l-.6.4c.4 1 1.1 1.8 2 2.3l.5-.5c.3-.3.7-.3 1-.1l1.4.9c.4.2.5.8.2 1.1l-.6.7c-.5.5-1.300.6-1.900.3C6.9 10.6 5.4 9 4.6 7c-.3-.7-.1-1.500.4-2z" fill="#fff"/></svg>
      763-555-0184
    </li>
    <li>
      <svg viewBox="0 0 16 16"><circle cx="8" cy="8" r="8" fill="var(--icon)"/><rect x="3.8" y="5.2" width="8.4" height="5.8" fill="#fff"/><path d="M3.8 5.2 8 8.4l4.2-3.2" fill="none" stroke="var(--icon)" stroke-width="0.9"/></svg>
      dana@meadowlark-cx.example
    </li>
    <li>
      <svg viewBox="0 0 16 16"><circle cx="8" cy="8" r="8" fill="var(--icon)"/><circle cx="8" cy="8" r="4.6" fill="none" stroke="#fff" stroke-width="1"/><path d="M3.4 8h9.2M8 3.4c-2 2.6-2 6.6 0 9.2M8 3.4c2 2.6 2 6.6 0 9.2" fill="none" stroke="#fff" stroke-width="0.8"/></svg>
      www.meadowlark-cx.example
    </li>
  </ul>
</section>

</body>
</html>
```